Placing my newer logo on my existing business card

I have a business card that I had you guys do years ago, then I changed my logo, I love both my business card and my logo. The challenge is both my logo and my business card are very similar in color. So I'm not sure how to make my logo stand out.

Sick

```html
<!DOCTYPE html>
<html lang="en">
<head>
<meta charset="utf-8">
<title>Business Card – Front and Back</title>
<link rel="stylesheet" href="https://fonts.googleapis.com/css2?family=Cinzel:wght@600&family=Questrial&family=Roboto:wght@400;700&display=swap">
<style>
  :root {
    --page-bg: #d8d9da;
    --card-bg: #eeedeb;
    --band-grey: #687174;
    --accent-red: #a3442f;
    --text-grey: #595f62;
    --icon-grey: #6f7679;
    --divider: #8b9194;
    --white: #ffffff;
  }
  * { box-sizing: border-box; margin: 0; padding: 0; }
  html, body { width: 1200px; height: 901px; overflow: hidden; }
  body { background: var(--page-bg); position: relative; font-family: "Questrial", sans-serif; }

  .card {
    position: absolute;
    left: 320px;
    width: 560px;
    height: 362px;
    background: var(--card-bg);
    overflow: hidden;
    box-shadow: 0 4px 10px rgba(0,0,0,0.18);
  }
  .card--front { top: 60px; }
  .card--back { top: 470px; }

  /* Front */
  .front__top-band { position: absolute; left: 0; top: 0; width: 100%; height: 76px; background: var(--band-grey); }
  .front__bottom-band { position: absolute; left: 0; bottom: 0; width: 100%; height: 11px; background: var(--band-grey); }
  .portrait {
    position: absolute; left: 193px; top: 20px; width: 86px; height: 86px; border-radius: 50%;
    border: 3px solid var(--accent-red); background: var(--white); padding: 3px;
  }
  .portrait__fill { width: 100%; height: 100%; border-radius: 50%; background: radial-gradient(circle at 50% 40%, #d8c39a 0%, #b9b4ad 45%, #e9e9e9 100%); }
  .divider { position: absolute; left: 235px; top: 132px; width: 2px; height: 176px; background: var(--divider); }

  .brand { position: absolute; left: 20px; top: 150px; width: 200px; text-align: center; }
  .brand__dot { width: 46px; height: 46px; border-radius: 50%; background: var(--band-grey); margin: 0 auto 14px; }
  .brand__name { font-family: "Roboto", sans-serif; font-weight: 700; font-size: 17px; line-height: 20px; color: var(--accent-red); }

  .person { position: absolute; right: 30px; top: 127px; text-align: right; }
  .person__name { font-family: "Roboto", sans-serif; font-weight: 700; font-size: 29px; color: var(--accent-red); letter-spacing: -0.3px; line-height: 32px; }
  .person__title { font-family: "Roboto", sans-serif; font-size: 12.5px; letter-spacing: 3px; color: var(--text-grey); margin-top: 2px; margin-right: -3px; }

  .contact { position: absolute; right: 26px; top: 226px; list-style: none; }
  .contact__item { display: flex; justify-content: flex-end; align-items: center; gap: 14px; color: var(--text-grey); font-size: 13px; line-height: 14px; text-align: right; margin-bottom: 6px; }
  .contact__item--phone { font-family: "Roboto", sans-serif; font-size: 13.5px; letter-spacing: 0.5px; }
  .contact__icon { width: 10px; height: 10px; flex: none; }

  /* Back */
  .back__header { position: absolute; left: 0; top: 0; width: 100%; height: 51px; background: var(--band-grey); display: flex; align-items: center; justify-content: center; }
  .back__title { font-family: "Cinzel", serif; font-weight: 600; font-size: 16.5px; color: var(--white); letter-spacing: 1px; }
  .conditions { position: absolute; top: 67px; list-style: none; }
  .conditions--left { left: 54px; }
  .conditions--right { left: 339px; }
  .conditions__item { font-size: 12.5px; line-height: 18.6px; color: var(--text-grey); padding-left: 11px; position: relative; }
  .conditions__item::before { content: ""; position: absolute; left: 0; top: 6px; width: 4px; height: 4px; background: #9ba0a3; transform: rotate(45deg); }

  .back__footer { position: absolute; left: 0; bottom: 0; width: 100%; height: 58px; background: var(--accent-red); }
  .footer-brand { position: absolute; left: 42px; top: 14px; display: flex; align-items: center; gap: 10px; }
  .footer-brand__dot { width: 30px; height: 30px; border-radius: 50%; background: var(--white); }
  .footer-brand__name { font-family: "Roboto", sans-serif; font-weight: 700; font-size: 14px; line-height: 16px; color: var(--white); }
  .footer-cta { position: absolute; right: 18px; top: 11px; text-align: center; color: var(--white); }
  .footer-cta__phone { font-family: "Roboto", sans-serif; font-weight: 700; font-size: 17px; line-height: 20px; }
  .footer-cta__web { font-size: 11.5px; margin-top: 2px; }
</style>
</head>
<body>

<section class="card card--front" aria-label="Card front">
  <div class="front__top-band"></div>
  <div class="portrait"><div class="portrait__fill" role="img" aria-label="Portrait photo of the director"></div></div>

  <div class="brand">
    <div class="brand__dot"></div>
    <p class="brand__name">Cedarline Wellness</p>
  </div>

  <div class="divider"></div>

  <div class="person">
    <h1 class="person__name">Marla Henderson</h1>
    <p class="person__title">DIRECTOR</p>
  </div>

  <ul class="contact">
    <li class="contact__item">
      <span>1420 Cedar Ridge Rd Ste#3<br>Maple Falls Utah 84012</span>
      <svg class="contact__icon" viewBox="0 0 10 10"><circle cx="5" cy="5" r="5" fill="var(--icon-grey)"/><circle cx="5" cy="4.3" r="1.6" fill="var(--card-bg)"/></svg>
    </li>
    <li class="contact__item contact__item--phone">
      <span>1(555)204-7719</span>
      <svg class="contact__icon" viewBox="0 0 10 10"><circle cx="5" cy="5" r="5" fill="var(--icon-grey)"/><path d="M3.2 2.6l1 .1.4 1.1-.6.5c.3.7.8 1.2 1.5 1.5l.5-.6 1.1.4.1 1c-2.3.2-4.2-1.7-4-4z" fill="var(--card-bg)"/></svg>
    </li>
    <li class="contact__item">
      <span>www.cedarlinewellness.com</span>
      <svg class="contact__icon" viewBox="0 0 10 10"><circle cx="5" cy="5" r="5" fill="var(--icon-grey)"/><circle cx="5" cy="5" r="2.8" fill="none" stroke="var(--card-bg)" stroke-width=".7"/><path d="M2.2 5h5.6M5 2.2v5.6" stroke="var(--card-bg)" stroke-width=".6"/></svg>
    </li>
  </ul>

  <div class="front__bottom-band"></div>
</section>

<section class="card card--back" aria-label="Card back">
  <header class="back__header"><h2 class="back__title">CONDITIONS WE ADDRESS FOR WOMEN AND MEN</h2></header>

  <ul class="conditions conditions--left">
    <li class="conditions__item">PCOS</li>
    <li class="conditions__item">Hysterectomy</li>
    <li class="conditions__item">Type-II Diabetes</li>
    <li class="conditions__item">Insulin Resistance</li>
    <li class="conditions__item">Hypothyroid</li>
    <li class="conditions__item">Underactive Thyroid</li>
    <li class="conditions__item">Fibromyalgia</li>
    <li class="conditions__item">Chronic Fatigue</li>
    <li class="conditions__item">Chronic Headaches &amp; Migraines</li>
    <li class="conditions__item">Hypertension</li>
    <li class="conditions__item">Elevated Fasting Glucose</li>
  </ul>

  <ul class="conditions conditions--right">
    <li class="conditions__item">Pre-Diabetes</li>
    <li class="conditions__item">Abdominal Obesity</li>
    <li class="conditions__item">High Triglycerides</li>
    <li class="conditions__item">High Blood Pressure</li>
    <li class="conditions__item">High Cholesterol</li>
    <li class="conditions__item">Gestational Diabetes</li>
    <li class="conditions__item">Epstein Bar</li>
    <li class="conditions__item">Infertility</li>
    <li class="conditions__item">Infertility Drugs</li>
    <li class="conditions__item">Anti-Depression Medication</li>
  </ul>

  <footer class="back__footer">
    <div class="footer-brand">
      <div class="footer-brand__dot"></div>
      <p class="footer-brand__name">Cedarline Wellness</p>
    </div>
    <div class="footer-cta">
      <p class="footer-cta__phone">Call Today!: (555)204-7719</p>
      <p class="footer-cta__web">www.cedarlinewellness.com</p>
    </div>
  </footer>
</section>

</body>
</html>
```